Luxury Business Card Design for High-End Window Treatments

Gilded Vantages
Custom Plantation Shutters & Architectural Shading Systems

⸻

BACK

Daniel Forsythe
Owner

Custom Interior & Exterior Window Treatments

919-482-7034
gildedvantages.com

I have included a picture that I’m hoping we can use on the back, but I’m also wondering if you can get rid of the ladder? Should we get rid of shutters , shades and blinds underneath Gilded Vantages?

Target Market(s)

High-end residential homeowners, custom home builders, architects, interior designers, and luxury renovation clients seeking premium plantation shutters and motorized architectural shading systems.

Industry/Entity Type

Custom Window treatments

Contact Information for Business Card

Front Gilded Vantages Custom Plantation Shutters Motorized Architectural Shading Systems BACK Daniel Forsythe Owner 919-482-7034 GildedVantages.com Custom Interior & Exterior Window Treatments By Appointment

Requirements
Nice to have
• Not 100% sure on nice to halves or the color but you can definitely check out my website to get a better understanding of what I’m trying to do

```html
<!DOCTYPE html>
<html lang="en">
<head>
<meta charset="utf-8">
<title>Gilded Vantages — Business Card</title>
<link href="https://fonts.googleapis.com/css2?family=Bodoni+Moda:opsz,wght@6..96,400;6..96,700&display=swap" rel="stylesheet">
<style>
  :root {
    --page: #ffffff;
    --front-bg: #000000;
    --back-bg: #ece8e1;
    --ink: #111111;
    --white: #ffffff;
    --gold: #a89a5f;
    --gold-bright: #c2ad6a;
  }
  * { margin: 0; padding: 0; box-sizing: border-box; }
  html, body {
    width: 1158px; height: 1200px; overflow: hidden;
    background: var(--page);
    font-family: "Bodoni Moda", "Times New Roman", serif;
  }
  .canvas { position: relative; width: 1158px; height: 1200px; }

  .card { position: absolute; overflow: hidden; }

  /* Front */
  .card-front {
    left: 232px; top: 125px; width: 703px; height: 404px;
    background: var(--front-bg);
    text-align: center;
  }
  .brand-name {
    position: absolute; left: 0; right: 0; top: 52px;
    color: var(--white); font-weight: 400;
    font-size: 46px; line-height: 56px; letter-spacing: 0.5px;
  }
  .brand-lines {
    position: absolute; left: 0; right: 0; top: 158px;
    color: var(--gold-bright); font-weight: 700;
    font-size: 19px; word-spacing: 12px;
  }
  .front-rule {
    position: absolute; left: 273px; top: 217px;
    width: 156px; height: 2px; background: var(--gold);
  }
  .front-tagline {
    position: absolute; left: 0; right: 0; top: 254px;
    color: var(--gold); font-size: 23px; line-height: 31px;
  }

  /* Back */
  .card-back {
    left: 235px; top: 657px; width: 701px; height: 402px;
    background: var(--back-bg); color: var(--ink);
  }
  .person-name {
    position: absolute; left: 33px; top: 30px;
    font-size: 33px; font-weight: 700; letter-spacing: 0.3px;
  }
  .person-role {
    position: absolute; left: 33px; top: 80px; font-size: 25px;
  }
  .services {
    position: absolute; left: 33px; top: 133px;
    font-size: 17.5px; line-height: 23px;
  }
  .back-rule {
    position: absolute; left: 33px; top: 218px;
    width: 156px; height: 2px; background: var(--ink);
  }
  .contact {
    position: absolute; left: 33px; display: flex; align-items: center;
    font-size: 23px; gap: 9px;
  }
  .contact svg { width: 23px; height: 23px; flex: none; }
  .contact-phone { top: 264px; }
  .contact-web { top: 303px; }

  .photo { position: absolute; border-radius: 13px; }
  .photo-porch {
    left: 320px; top: 19px; width: 353px; height: 243px;
    background: linear-gradient(180deg, #5d8fd6 0%, #8fb3e3 25%, #3b3f48 45%, #2b2e34 65%, #5a6048 85%, #3f4a2c 100%);
  }
  .photo-shutters {
    left: 320px; top: 274px; width: 110px; height: 109px;
    background: linear-gradient(135deg, #6a3f2a, #b08866 55%, #e6e2dc);
  }
  .photo-blinds {
    left: 441px; top: 274px; width: 110px; height: 109px;
    background: linear-gradient(180deg, #d9d4cd, #f2f0ec 60%, #cfc9bf);
  }
  .photo-bedroom {
    left: 564px; top: 274px; width: 110px; height: 109px;
    background: linear-gradient(160deg, #7c7b79, #b7b4ae 55%, #ddd8cf);
  }
</style>
</head>
<body>
<main class="canvas">

  <section class="card card-front" aria-label="Card front">
    <h1 class="brand-name">Gilded<br>Vantages</h1>
    <p class="brand-lines">Shutters Shades Blinds</p>
    <div class="front-rule"></div>
    <p class="front-tagline">Custom Plantation Shutters &amp; Motorized<br>Architectural Shading Systems</p>
  </section>

  <section class="card card-back" aria-label="Card back">
    <h2 class="person-name">Daniel Forsythe</h2>
    <p class="person-role">Owner</p>
    <p class="services">Custom Interior &amp; Exterior<br>Window Treatments</p>
    <div class="back-rule"></div>

    <p class="contact contact-phone">
      <svg viewBox="0 0 24 24" fill="none" stroke="currentColor" stroke-width="1.8" stroke-linejoin="round">
        <path d="M5 2.5h4l2 5-2.5 1.5a11 11 0 0 0 6.5 6.5L16.5 13l5 2v4a2 2 0 0 1-2 2A17 17 0 0 1 3 4.5a2 2 0 0 1 2-2z"/>
      </svg>
      919-482-7034
    </p>
    <p class="contact contact-web">
      <svg viewBox="0 0 24 24" fill="none" stroke="currentColor" stroke-width="1.8">
        <circle cx="12" cy="12" r="10"/>
        <ellipse cx="12" cy="12" rx="4.5" ry="10"/>
        <path d="M2 12h20M4 7h16M4 17h16"/>
      </svg>
      gildedvantages.com
    </p>

    <div class="photo photo-porch" role="img" aria-label="Covered back porch of a home fitted with dark motorized exterior screens under a blue sky"></div>
    <div class="photo photo-shutters" role="img" aria-label="Interior room with wooden plantation shutters"></div>
    <div class="photo photo-blinds" role="img" aria-label="Bright living room window with light horizontal blinds"></div>
    <div class="photo photo-bedroom" role="img" aria-label="Bedroom with soft window shades"></div>
  </section>

</main>
</body>
</html>
```